Quillfern Litigation Funding Letterhead & Document Template

We need a letter head designed for our fund. Our fund works with law firms and investors across the globe. We need a a cover letter template as well as a document template for subsequent pages. Blue and white color scheme is preferred. This is our predecessor's website: https://www.quillfernlc.com/index.html. Please see our logo attached. The logo color code is #19478d. Font is Gotham-Medium.
Target Market(s)
Sophisticated investors and law firms
Font styles to use
Sans Serif
Colors
0255a3

```html
<!DOCTYPE html>
<html lang="en">
<head>
<meta charset="utf-8">
<title>Quillfern Litigation Funding – Stationery</title>
<link href="https://fonts.googleapis.com/css2?family=Lato:wght@400;700&family=Open+Sans:wght@400;500&display=swap" rel="stylesheet">
<style>
  :root {
    --brand-blue: #19478d;
    --band-blue: #0d4593;
    --paper: #ffffff;
    --backdrop: #e4e5e7;
    --ink: #3f3f3f;
    --ink-soft: #555555;
  }
  * { box-sizing: border-box; margin: 0; padding: 0; }
  html, body { width: 1200px; height: 1200px; overflow: hidden; }
  body { background: var(--backdrop); position: relative; font-family: "Open Sans", sans-serif; }

  .letterhead {
    position: absolute; left: 60px; top: 150px; width: 640px; height: 822px;
    background: var(--paper); box-shadow: 0 2px 10px rgba(0,0,0,.15);
  }
  .letterhead__band {
    position: absolute; left: 0; right: 0; top: 26px; height: 11px; background: var(--band-blue);
  }
  .brand-name {
    font-family: "Lato", sans-serif; font-weight: 700; color: var(--brand-blue);
    letter-spacing: .04em; text-transform: uppercase; white-space: nowrap;
  }
  .letterhead__brand {
    position: absolute; top: 56px; left: 0; right: 0; text-align: center; font-size: 13px;
  }
  .letterhead__body {
    position: absolute; left: 61px; right: 62px; top: 148px;
    font-size: 10.2px; color: var(--ink); line-height: 1.25;
  }
  .letter-date { margin-bottom: 12px; }
  .letter-recipient { margin-bottom: 34px; }
  .letter-salutation { margin-bottom: 26px; }
  .letter-paragraph { text-align: justify; line-height: 18.4px; margin-bottom: 18px; }
  .letter-closing { margin-top: 38px; }
  .letter-signature {
    display: block; width: 145px; height: 18px; margin: 8px 0 10px;
    background: linear-gradient(90deg, rgba(80,80,80,.35), rgba(80,80,80,.12));
    border-radius: 9px;
  }
  .signer-name { font-size: 12.5px; font-weight: 500; color: #333; }
  .signer-title { margin-top: 4px; color: var(--ink-soft); }

  .letterhead__footer {
    position: absolute; left: 0; right: 0; bottom: 0; height: 70px;
  }
  .footer-mark {
    position: absolute; left: 22px; bottom: 12px; width: 40px; height: 40px; background: var(--band-blue);
  }
  .footer-band {
    position: absolute; right: 0; bottom: 0; width: 555px; height: 46px; background: var(--band-blue);
    clip-path: polygon(0 0, 100% 0, 100% 100%, 22px 100%);
    color: #fff; font-family: "Lato", sans-serif; font-size: 12px; text-align: center;
    padding-left: 30px; padding-right: 110px;
  }
  .footer-address {
    padding-top: 4px; padding-bottom: 2px; border-bottom: 1px solid rgba(255,255,255,.7);
    margin: 0 20px;
  }
  .footer-contact { padding-top: 3px; }

  .envelope {
    position: absolute; left: 740px; width: 400px; height: 200px; background: var(--paper);
    box-shadow: 0 2px 8px rgba(0,0,0,.15); overflow: hidden;
  }
  .envelope--front { top: 460px; }
  .envelope--back { top: 690px; }
  .envelope__brand { position: absolute; left: 22px; top: 48px; font-size: 10px; }
  .envelope__band {
    position: absolute; right: 0; bottom: 0; width: 360px; height: 26px; background: var(--band-blue);
    clip-path: polygon(0 0, 100% 0, 100% 100%, 14px 100%);
    color: #fff; font-family: "Lato", sans-serif; font-size: 7.5px; line-height: 26px; padding-left: 48px;
  }
  .envelope__mark {
    position: absolute; left: 4px; bottom: 4px; width: 26px; height: 26px; background: var(--band-blue);
  }
  .envelope__flap {
    position: absolute; left: 0; right: 0; top: 0; height: 47px; background: var(--band-blue);
    clip-path: polygon(0 0, 100% 0, 96% 100%, 4% 100%);
    display: flex; align-items: center; justify-content: center;
  }
  .envelope__flap .brand-name { color: #fff; font-size: 11px; }
</style>
</head>
<body>
  <article class="letterhead">
    <div class="letterhead__band"></div>
    <div class="letterhead__brand brand-name">Quillfern Litigation Funding</div>

    <div class="letterhead__body">
      <p class="letter-date">Issuing Date: May 5, 2018</p>
      <p class="letter-recipient">Name Of Employee Mr. XYZABC<br>Address of Employee<br>Address Line 2 etc..</p>
      <p class="letter-salutation">Dear Mr.XYZABC</p>
      <p class="letter-paragraph">Lorem Ipsum has been the industry's standard dummy text ever since the 1500s, when an unknown printer took a galley of type and scrambled it to make a type specimen book. It has survived not only five centuries, but also the leap into electronic typesetting, remaining essentially unchanged. It was popularised in the 1960s with the release of Letraset sheets containing Lorem Ipsum passages, and more recently with desktop publishing software like Aldus PageMaker including versions of Lorem Ipsum.</p>
      <p class="letter-paragraph">Lorem Ipsum is simply dummy text of the printing and typesetting industry. Lorem Ipsum has been the industry's standard dummy text ever since the 1500s, when an unknown printer took a galley of type and scrambled it to make a type specimen book.</p>
      <p class="letter-paragraph">It has survived not only five centuries, but also the leap into electronic typesetting, remaining essentially unchanged. It was popularised in the 1960s with the release of Letraset sheets containing Lorem Ipsum passages.</p>
      <p class="letter-closing">Yours Sincerely</p>
      <span class="letter-signature" role="img" aria-label="Handwritten signature of Dorian Keller"></span>
      <p class="signer-name">Dorian Keller</p>
      <p class="signer-title">Managing Director</p>
    </div>

    <footer class="letterhead__footer">
      <div class="footer-mark"></div>
      <div class="footer-band">
        <p class="footer-address">421, Address line goes here Country Name, 45452</p>
        <p class="footer-contact">P: 044-123 456 789 | E: info@webname.com | www.websitename.com</p>
      </div>
    </footer>
  </article>

  <section class="envelope envelope--front">
    <div class="envelope__brand brand-name">Quillfern Litigation Funding</div>
    <div class="envelope__band">421, Address line goes here Country Name, Country code 45452</div>
    <div class="envelope__mark"></div>
  </section>

  <section class="envelope envelope--back">
    <div class="envelope__flap"><span class="brand-name">Quillfern Litigation Funding</span></div>
  </section>
</body>
</html>
```